Info flyer to showcase security camera install and remote video monitoring.

I am looking for an attractive looking flyer that is simple and has some text content and some photos to show prospective clients what services I can provide them.

The two main services that I want to showcase are:
1. Security Camera & NVR Installations and maintenance
2. Remote Video Monitoring for business. This can be a temporary service or ongoing/long term.

Target Market(s)

Construction, Retail, Industrial, Commercial

Industry/Entity Type

Security

Font styles to use
Serif

Colors

Designer to choose colors to be used in the design.

```html
<!DOCTYPE html>
<html lang="en">
<head>
<meta charset="utf-8">
<title>Sentrylane – Security Camera &amp; NVR Flyer</title>
<link rel="stylesheet" href="https://fonts.googleapis.com/css2?family=Anton&family=Montserrat:wght@500;600;700&display=swap">
<style>
  :root {
    --stage: #4b4b4d;
    --paper: #ffffff;
    --gold: #c9a12e;
    --gold-mid: #b9922b;
    --gold-deep: #a9852a;
    --gold-faint: #bb952a;
    --ink: #2a2a2a;
    --sky-top: #2a78c8;
    --sky-bottom: #4c95d9;
  }
  * { margin: 0; padding: 0; box-sizing: border-box; }
  html, body { width: 801px; height: 1200px; overflow: hidden; }
  body { background: var(--stage); position: relative; }

  .flyer {
    position: absolute; left: 40px; top: 134px;
    width: 504px; height: 652px;
    transform: scale(1.4286); transform-origin: 0 0;
    background: var(--paper);
    font-family: "Montserrat", sans-serif;
    overflow: hidden;
  }

  .brand { position: absolute; left: 0; top: 0; width: 504px; height: 118px;
    display: flex; align-items: center; justify-content: center; }
  .brand-name { font-weight: 600; font-size: 31px; letter-spacing: 1px; line-height: 1; color: var(--ink); }

  .intro-band { position: absolute; left: 0; top: 118px; width: 278px; height: 140px; background: var(--gold); }
  .intro-band p { position: absolute; left: 38px; top: 24px; font-size: 18px; line-height: 24px;
    font-weight: 600; color: var(--gold-faint); }

  .photo-interior { position: absolute; left: 260px; top: 118px; width: 244px; height: 140px;
    background: linear-gradient(135deg, #8fa0b0 0%, #c9d2da 45%, #5d6b80 100%); }
  .photo-poles { position: absolute; left: 0; top: 258px; }

  .headline { position: absolute; right: 18px; top: 304px; text-align: right;
    font-family: "Anton", sans-serif; font-weight: 400; color: var(--ink);
    font-size: 28px; line-height: 42px; letter-spacing: -0.5px; }
  .service-bar { position: absolute; left: 274px; top: 403px; width: 230px; height: 20px;
    background: var(--gold); color: #fff; font-family: "Anton", sans-serif; font-size: 10px;
    line-height: 20px; text-align: right; padding-right: 18px; letter-spacing: 0.2px; }
  .subhead { position: absolute; right: 18px; top: 448px; text-align: right;
    font-family: "Anton", sans-serif; font-weight: 400; color: var(--ink);
    font-size: 15px; line-height: 24px; letter-spacing: -0.3px; }
  .note { position: absolute; right: 18px; top: 506px; text-align: right;
    font-family: "Anton", sans-serif; color: var(--gold); font-size: 7px; line-height: 11px; }

  .rule { position: absolute; left: 0; top: 558px; width: 504px; height: 4px; background: var(--gold); }

  .contact { position: absolute; left: 0; top: 568px; width: 504px; height: 84px; display: flex; }
  .contact-item { flex: 1; display: flex; flex-direction: column; align-items: center;
    justify-content: center; gap: 9px; color: #fff; font-size: 5px; line-height: 7px; text-align: center; }
  .contact-item.address { background: var(--gold); }
  .contact-item.phone { background: var(--gold-mid); }
  .contact-item.email { background: var(--gold-deep); }
  .contact-item svg { width: 16px; height: 16px; fill: #fff; }
</style>
</head>
<body>
  <main class="flyer">
    <header class="brand">
      <span class="brand-name">SENTRYLANE</span>
    </header>

    <section class="intro-band"><p>Remote Video<br>Monitoring<br>for business.</p></section>
    <div class="photo-interior" role="img" aria-label="Dome security camera mounted in a bright shopping centre"></div>

    <svg class="photo-poles" width="300" height="302" viewBox="0 0 300 302" role="img" aria-label="Security cameras mounted on a pole against a blue sky">
      <defs>
        <linearGradient id="sky" x1="0" y1="0" x2="0" y2="1">
          <stop offset="0" stop-color="var(--sky-top)"/>
          <stop offset="1" stop-color="var(--sky-bottom)"/>
        </linearGradient>
      </defs>
      <path d="M0 0 H279 Q292 150 249 300 H0 Z" fill="url(#sky)"/>
    </svg>

    <h1 class="headline">Security Camera<br>&amp; NVR</h1>
    <div class="service-bar">Installations and Maintenance</div>
    <h2 class="subhead">Remote Video Monitoring<br>for business.</h2>
    <p class="note">This can be a temporary service<br>or ongoing/long term.</p>

    <div class="rule"></div>

    <footer class="contact">
      <div class="contact-item address">
        <svg viewBox="0 0 24 24"><path d="M12 2a7 7 0 0 0-7 7c0 5 7 13 7 13s7-8 7-13a7 7 0 0 0-7-7zm0 9.5A2.5 2.5 0 1 1 12 6.5a2.5 2.5 0 0 1 0 5z"/></svg>
        <span>Lorem Ipsum, Lorem Ipsum<br>Lorem Ipsum Lorem</span>
      </div>
      <div class="contact-item phone">
        <svg viewBox="0 0 24 24"><path d="M6.6 10.8a15.1 15.1 0 0 0 6.6 6.6l2.2-2.2a1 1 0 0 1 1-.25 11.4 11.4 0 0 0 3.6.57 1 1 0 0 1 1 1V20a1 1 0 0 1-1 1A17 17 0 0 1 3 4a1 1 0 0 1 1-1h3.5a1 1 0 0 1 1 1c0 1.25.2 2.45.57 3.57a1 1 0 0 1-.25 1z"/></svg>
        <span>000 000 0000<br>000 000 0000</span>
      </div>
      <div class="contact-item email">
        <svg viewBox="0 0 24 24"><path d="M2 5h20v14H2z M2 5l10 8 10-8" fill="none" stroke="#fff" stroke-width="2"/></svg>
        <span>hello@sentrylane.com</span>
      </div>
    </footer>
  </main>
</body>
</html>
```